Poetry Book Cover Design Project

Looking for a minimalistic book cover design for a collection of poems. The book title is "Where The Lanterns Drift Slowly Apart". There are three parts to the book. First covers poetry in the theme of Rage. Second love and desire. The third is strange poems. Essentially the sections are "Rage", "Desire" and the "Strange". The reason for the title "Where The Lanterns Drift Slowly Apart" is as if someone is writing these till life changes towards the intended outcome as felt in each poem. I want to have the author's name "Nuwanthi Karunasekera" at the bottom. Ilustration attached.
- Minimalistic

```html
<!DOCTYPE html>
<html lang="en">
<head>
<meta charset="utf-8">
<title>Where The Lanterns Drift Slowly Apart — Cover</title>
<link rel="stylesheet" href="https://fonts.googleapis.com/css2?family=Oswald:wght@600;700&family=Great+Vibes&display=swap">
<style>
  :root {
    --page-bg: #ffffff;
    --cover-deep: #0b2444;
    --cover-mid: #123a66;
    --cover-glow: #2a66a8;
    --silver-light: #f4f6f8;
    --silver-mid: #c9ced4;
    --silver-dark: #9aa3ad;
  }
  * { margin: 0; padding: 0; box-sizing: border-box; }
  html, body {
    width: 1200px;
    height: 1190px;
    overflow: hidden;
    background: var(--page-bg);
  }
  .canvas {
    position: relative;
    width: 1200px;
    height: 1190px;
  }
  .cover {
    position: absolute;
    left: 270px;
    top: 97px;
    width: 655px;
    height: 974px;
    overflow: hidden;
    background:
      radial-gradient(ellipse at 50% 40%, var(--cover-mid) 0%, var(--cover-deep) 75%);
  }
  .cover-art {
    position: absolute;
    inset: 0;
    background:
      radial-gradient(circle at 329px 300px, var(--cover-glow) 0%, rgba(42,102,168,0.55) 22%, rgba(18,58,102,0) 42%),
      radial-gradient(ellipse 60% 25% at 75% 85%, rgba(154,163,173,0.18) 0%, rgba(154,163,173,0) 100%);
  }
  .title {
    position: absolute;
    left: 0;
    width: 100%;
    top: 0;
    text-align: center;
    color: var(--silver-light);
  }
  .title-line {
    position: absolute;
    width: 100%;
    left: 0;
    text-align: center;
    background: linear-gradient(180deg, var(--silver-light) 0%, var(--silver-mid) 60%, var(--silver-dark) 100%);
    -webkit-background-clip: text;
    background-clip: text;
    color: transparent;
    text-shadow: 0 2px 3px rgba(0,0,0,0.25);
  }
  .title-top {
    top: 290px;
    font-family: 'Oswald', sans-serif;
    font-weight: 700;
    font-size: 40px;
    letter-spacing: -0.5px;
    line-height: 1;
  }
  .title-mid {
    top: 342px;
    font-family: 'Oswald', sans-serif;
    font-weight: 600;
    font-size: 30px;
    line-height: 1;
  }
  .title-script {
    top: 368px;
    font-family: 'Great Vibes', cursive;
    font-size: 74px;
    line-height: 1.1;
  }
  .author {
    position: absolute;
    left: 0;
    width: 100%;
    top: 790px;
    text-align: center;
    font-family: 'Oswald', sans-serif;
    font-weight: 700;
    line-height: 1.05;
    color: var(--silver-mid);
    text-shadow: 0 2px 3px rgba(0,0,0,0.3);
  }
  .author-first {
    display: block;
    font-size: 30px;
  }
  .author-last {
    display: block;
    font-size: 38px;
    color: var(--silver-light);
  }
</style>
</head>
<body>
  <div class="canvas">
    <div class="cover">
      <div class="cover-art" role="img" aria-label="Silver magnifying glass illustration with its reflection below"></div>
      <div class="title">
        <div class="title-line title-top">Where The Lanterns</div>
        <div class="title-line title-mid">Drift</div>
        <div class="title-line title-script">Slowly Apart</div>
      </div>
      <div class="author">
        <span class="author-first">Nuwanthi</span>
        <span class="author-last">Karunasekera</span>
      </div>
    </div>
  </div>
</body>
</html>
```